Pebblemoor Supplements

Hi WP designers, this is my first time trying Pixel Bazaar ;-)

I would like a responsive woocommerce/wordpress theme for a company called Pebblemoor supplements. You can get an idea of what we sell, and how bad our old site is here:http://www.pebblemoorsupplements-example.com.sg/

Would love to see any type of modern looking design, a few guidelines:
- We've got a logo (see attached)
- We like green as a base for the colour scheme to match the logo but open to ideas

Target Market(s)

90% of customers will be Singaporean looking for good deals on top brands they already buy.

Industry/Entity Type

It Company

Font styles to use
Other font styles liked:
• Open Sans

Colors
9bcb3c
add136
cadf82
0492cd
eb1f27
a6459a
f78f20
ffc214

Requirements
Must have
• Sign In/Sign UpNewsletter sign up: best dealsFeatured deals sectionRatings/Reviews on products
Nice to have
• We're open to any ideas but would perhaps like to see something minimalist and easy on the eyes.
• Try to keep mostly images and white space
Should not have
• Too much text

```html
<!DOCTYPE html>
<html lang="en">
<head>
<meta charset="utf-8">
<title>Pebblemoor Supplements</title>
<link rel="stylesheet" href="https://fonts.googleapis.com/css2?family=Oxygen:wght@300;400;700&family=Open+Sans:wght@400&display=swap">
<style>
:root{
  --green:#9bcb3c;
  --green-dark:#86b52c;
  --purple:#a6459a;
  --purple-dark:#8c3582;
  --blue:#2e8fd6;
  --ink:#333;
  --muted:#555;
  --line:#e2e2e2;
  --footer:#2b2b2b;
  --footer-text:#cfcfcf;
  --white:#fff;
}
*{margin:0;padding:0;box-sizing:border-box}
html,body{width:1200px;height:2371px;overflow:hidden;background:var(--white)}
body{position:relative;font-family:"Oxygen",sans-serif;color:var(--ink)}
.abs{position:absolute}

.topbar{left:0;top:0;width:1200px;height:70px;background:var(--green);color:var(--white);font-size:14px}
.topbar .account{left:86px;top:30px}
.topbar .cart{left:788px;top:30px;display:flex;align-items:center;gap:8px}
.topbar .auth{left:981px;top:30px}
.topbar span.sep{margin:0 8px}

.header-arc{left:464px;top:0;width:272px;height:160px}
.brand{left:0;top:162px;width:1200px;text-align:center;font-weight:300;font-size:46px;letter-spacing:1px;color:#222}

.nav{left:0;top:266px;width:1200px;height:55px;background:linear-gradient(var(--purple),var(--purple-dark));display:flex;padding-left:94px}
.nav a{display:flex;align-items:center;justify-content:center;color:var(--white);text-decoration:none;font-size:17px;border-right:1px solid rgba(0,0,0,.18);box-shadow:1px 0 0 rgba(255,255,255,.15)}
.nav a:last-child{border-right:none;box-shadow:none}

.hero{left:0;top:321px;width:1200px;height:464px;background:linear-gradient(100deg,#3d7fae 0%,#6aa6cc 35%,#b9c9d2 60%,#e8dcd2 80%,#9bb8cc 100%)}
.hero-arrow{width:62px;height:62px;border-radius:50%;top:517px;display:flex;align-items:center;justify-content:center}
.hero-arrow.prev{left:86px;background:rgba(40,70,95,.55)}
.hero-arrow.next{left:1052px;background:rgba(255,255,255,.18)}

.band{left:0;top:785px;width:1200px;height:151px;background:var(--green)}
.band h2{left:116px;top:826px;font-size:29px;font-weight:700;color:var(--white);letter-spacing:.5px}
.band .divider{left:442px;top:818px;width:1px;height:52px;background:rgba(255,255,255,.45)}
.band p{left:477px;top:818px;width:620px;font-size:15px;line-height:27px;color:var(--white)}

.brands{left:86px;top:901px;width:1028px;height:230px;background:var(--white);box-shadow:0 3px 10px rgba(0,0,0,.12);border-radius:4px}
.brand-card{top:916px;width:317px;height:183px;border-radius:5px;overflow:hidden}
.brand-card .photo{position:absolute;inset:0}
.brand-card .label{position:absolute;left:0;bottom:0;width:100%;height:44px;background:rgba(40,40,40,.72);color:var(--white);font-size:19px;display:flex;align-items:center;justify-content:space-between;padding:0 16px 0 18px}

.section-title{left:86px;font-size:30px;font-weight:400;color:var(--purple)}

.product{width:222px;height:280px;border:1px solid var(--line);background:var(--white)}
.product .shot{position:absolute;left:65px;top:26px;width:92px;height:128px;border-radius:12px 12px 8px 8px}
.product .name{position:absolute;left:0;top:176px;width:100%;text-align:center;font-size:15.5px;line-height:26px;color:#444}
.product .price{position:absolute;left:26px;top:236px;font-size:15.5px;color:#333}
.product .stars{position:absolute;right:22px;top:235px;font-size:14px;letter-spacing:2px;color:#999}

.footer{left:0;top:1997px;width:1200px;height:374px;background:var(--footer);color:var(--footer-text)}
.footer h3{font-weight:400;font-size:20px;color:var(--white)}
.footer ul{list-style:none;font-size:14.5px;line-height:28.5px}
.footer p{font-size:14.5px;line-height:28px}
.news-input{left:541px;top:2143px;width:268px;height:39px;background:var(--white);border:none}
.subscribe{left:679px;top:2204px;width:130px;height:40px;background:var(--blue);color:var(--white);font-size:17px;display:flex;align-items:center;justify-content:center}
.social{top:2142px;width:28px;height:28px;border-radius:50%;background:#666}
.footer-rule{left:0;top:2275px;width:1200px;height:1px;background:#3d3d3d}
.copyright{left:86px;top:2310px;font-family:"Open Sans",sans-serif;font-size:14px;color:var(--white)}
.pay{top:2305px;width:46px;height:28px;border-radius:3px;background:var(--white)}
</style>
</head>
<body>

<div class="abs topbar">
  <div class="abs account">REGISTER<span class="sep">|</span>LOGIN<span class="sep">|</span>MY ACCOUNT</div>
  <div class="abs cart">
    <svg width="18" height="16" viewBox="0 0 18 16"><path d="M1 2h3l2 8h9l2-6H5" fill="none" stroke="#fff" stroke-width="1.8"/><circle cx="7" cy="13.5" r="1.5" fill="#fff"/><circle cx="14" cy="13.5" r="1.5" fill="#fff"/></svg>
    CART (0) ITEMS
  </div>
  <div class="abs auth">SIGN IN<span class="sep">|</span>SIGN UP</div>
</div>

<svg class="abs header-arc" viewBox="0 0 272 160"><path d="M4 160 A132 132 0 0 1 268 160" fill="var(--white)" stroke="var(--green)" stroke-width="5"/><path d="M0 0 H272 V68 H0Z" fill="none"/></svg>
<div class="abs brand">PEBBLEMOOR SUPPLEMENTS</div>

<nav class="abs nav">
  <a style="width:117px">HOME</a>
  <a style="width:152px">ABOUT US</a>
  <a style="width:171px">CATEGORIES</a>
  <a style="width:183px">TESTIMONIALS</a>
  <a style="width:224px">SPECIAL PRODUCTS</a>
  <a style="width:176px">CONTACT US</a>
</nav>

<div class="abs hero" role="img" aria-label="Smiling woman with raised arms against a blue sky"></div>
<div class="abs hero-arrow prev"><svg width="14" height="24" viewBox="0 0 14 24"><path d="M12 2 2 12l10 10" fill="none" stroke="#fff" stroke-width="2"/></svg></div>
<div class="abs hero-arrow next"><svg width="14" height="24" viewBox="0 0 14 24"><path d="M2 2l10 10L2 22" fill="none" stroke="#fff" stroke-width="2"/></svg></div>

<div class="abs band"></div>
<h2 class="abs band" style="all:unset;position:absolute;left:116px;top:826px;font-size:29px;font-weight:700;color:#fff;letter-spacing:.5px;font-family:'Oxygen',sans-serif">NIRUM EST NOTARE</h2>
<div class="abs" style="left:442px;top:818px;width:1px;height:52px;background:rgba(255,255,255,.45)"></div>
<p class="abs" style="left:477px;top:818px;width:620px;font-size:15px;line-height:27px;color:#fff">Jerta baditaut onsequser untur magni dolores eoquie voluptate msequi nesciunt volup tatem accusantium dolorem consectetuer adipiscing elit aenean.</p>

<div class="abs brands"></div>
<div class="abs brand-card" style="left:101px">
  <div class="photo" role="img" aria-label="Supplement bottles on a pharmacy shelf" style="background:linear-gradient(#6b7d8a,#8a5a3a 60%,#3b2d26)"></div>
  <div class="label">HALVORSEN<svg width="26" height="26" viewBox="0 0 26 26"><circle cx="13" cy="13" r="11" fill="none" stroke="#fff" stroke-width="1.6"/><path d="M11 8l5 5-5 5" fill="none" stroke="#fff" stroke-width="1.6"/></svg></div>
</div>
<div class="abs brand-card" style="left:442px">
  <div class="photo" role="img" aria-label="Row of green supplement tubs" style="background:linear-gradient(#0f4a36,#1d6b4d 55%,#0c2e23)"></div>
  <div class="label">MEADOWLIGHT<svg width="26" height="26" viewBox="0 0 26 26"><circle cx="13" cy="13" r="11" fill="none" stroke="#fff" stroke-width="1.6"/><path d="M11 8l5 5-5 5" fill="none" stroke="#fff" stroke-width="1.6"/></svg></div>
</div>
<div class="abs brand-card" style="left:782px">
  <div class="photo" role="img" aria-label="Orange pill bottles held by a pharmacist" style="background:linear-gradient(90deg,#e8e2d6,#f2b64a 45%,#e89a20 65%,#d9dde2)"></div>
  <div class="label">CORVANE<svg width="26" height="26" viewBox="0 0 26 26"><circle cx="13" cy="13" r="11" fill="none" stroke="#fff" stroke-width="1.6"/><path d="M11 8l5 5-5 5" fill="none" stroke="#fff" stroke-width="1.6"/></svg></div>
</div>

<h2 class="abs section-title" style="top:1164px">BEST DEALS</h2>

<div class="abs product" style="left:86px;top:1229px"><div class="shot" role="img" aria-label="Red-labelled supplement bottle" style="background:linear-gradient(#3a2a20 25%,#b8232a 25%,#8c1c20)"></div><div class="name">HALVORSEN<br>COQ10 150MG CAPS 30</div><div class="price">$119.50</div><div class="stars">☆☆☆☆☆</div></div>
<div class="abs product" style="left:354px;top:1229px"><div class="shot" role="img" aria-label="Teal-labelled supplement bottle" style="background:linear-gradient(#3a2a20 25%,#4fb3c6 25%,#2b8799)"></div><div class="name">HALVORSEN<br>COQ10 150MG CAPS 30</div><div class="price">$119.50</div><div class="stars">☆☆☆☆☆</div></div>
<div class="abs product" style="left:620px;top:1229px"><div class="shot" role="img" aria-label="White tub with red label" style="background:linear-gradient(#e8e8e8 22%,#e23a34 22%,#c42620 80%,#eee 80%)"></div><div class="name">HALVORSEN<br>COQ10 150MG CAPS 30</div><div class="price">$119.50</div><div class="stars">☆☆☆☆☆</div></div>
<div class="abs product" style="left:890px;top:1229px"><div class="shot" role="img" aria-label="Blue-labelled supplement bottle" style="background:linear-gradient(#3a2a20 25%,#1e4fa0 25%,#13306a)"></div><div class="name">HALVORSEN<br>COQ10 150MG CAPS 30</div><div class="price">$119.50</div><div class="stars">☆☆☆☆☆</div></div>

<h2 class="abs section-title" style="top:1575px">FEATURED DEALS</h2>

<div class="abs product" style="left:86px;top:1639px"><div class="shot" role="img" aria-label="Red-labelled supplement bottle" style="background:linear-gradient(#3a2a20 25%,#b8232a 25%,#8c1c20)"></div><div class="name">HALVORSEN<br>COQ10 150MG CAPS 30</div><div class="price">$119.50</div><div class="stars">☆☆☆☆☆</div></div>
<div class="abs product" style="left:354px;top:1639px"><div class="shot" role="img" aria-label="Teal-labelled supplement bottle" style="background:linear-gradient(#3a2a20 25%,#4fb3c6 25%,#2b8799)"></div><div class="name">HALVORSEN<br>COQ10 150MG CAPS 30</div><div class="price">$119.50</div><div class="stars">☆☆☆☆☆</div></div>
<div class="abs product" style="left:620px;top:1639px"><div class="shot" role="img" aria-label="White tub with red label" style="background:linear-gradient(#e8e8e8 22%,#e23a34 22%,#c42620 80%,#eee 80%)"></div><div class="name">HALVORSEN<br>COQ10 150MG CAPS 30</div><div class="price">$119.50</div><div class="stars">☆☆☆☆☆</div></div>
<div class="abs product" style="left:890px;top:1639px"><div class="shot" role="img" aria-label="Blue-labelled supplement bottle" style="background:linear-gradient(#3a2a20 25%,#1e4fa0 25%,#13306a)"></div><div class="name">HALVORSEN<br>COQ10 150MG CAPS 30</div><div class="price">$119.50</div><div class="stars">☆☆☆☆☆</div></div>

<footer class="abs footer">
  <h3 class="abs" style="left:86px;top:40px">Quick Links</h3>
  <ul class="abs" style="left:88px;top:76px">
    <li>Nam liber tempor</li><li>Typi non haben</li><li>Claritas est etiaprocess</li><li>Ending Soon</li><li>Quam nunc putamut</li>
  </ul>
  <h3 class="abs" style="left:330px;top:40px">About</h3>
  <ul class="abs" style="left:332px;top:76px">
    <li>About us</li><li>Contact Us</li><li>Help</li><li>Privacy Policy</li><li>Terms Of Service</li>
  </ul>
  <h3 class="abs" style="left:541px;top:40px">Newsletter</h3>
  <p class="abs" style="left:541px;top:76px;width:300px">Stay in touch with us by signing up for our quarterly newsletter!</p>
  <h3 class="abs" style="left:886px;top:40px">Follow us</h3>
  <p class="abs" style="left:886px;top:76px;width:240px;line-height:24px">Follow our news and events through social networks</p>
</footer>
<div class="abs news-input"></div>
<div class="abs subscribe">SUBSCRIBE</div>
<div class="abs social" style="left:887px"></div>
<div class="abs social" style="left:924px"></div>
<div class="abs social" style="left:962px"></div>
<div class="abs social" style="left:1000px"></div>
<div class="abs footer-rule"></div>
<div class="abs copyright">Copyright ©2013. All Rights Reserved.</div>
<div class="abs pay" style="left:861px"></div>
<div class="abs pay" style="left:912px"></div>
<div class="abs pay" style="left:963px"></div>
<div class="abs pay" style="left:1014px"></div>
<div class="abs pay" style="left:1066px"></div>

</body>
</html>
```